依頼詳細
チラシは主にポスティングで使用します。メインターゲット以外の層も集客していきたいので、あまり尖った訴求ではなく、メインターゲットに刺さりつつ、男性女性関係なく、効果的に集客できるチラシのデザインが希望です。今回のチラシの目的は、公式LINEの登録か、電話でのお問い合わせへ誘導することです。
記載項目
サロン名:髪のフォローアップサロン Tavi /電話番号:0952314862 /住所:佐賀県佐賀市東原町大字桜沢418-6 /キャッチココピー:あなたの髪を、毎日サロン帰りの髪に /オープン日:7月1日OPEN!! /予約受付開始:6月24日 /あなたのご来店を楽しみにお待ちしております! /メニュー表:PDFを別途添付します。全部載せるのか、いくつかピックアップして載せるのか相談しながらでお願いします。(メニューの内容も調整中ですので、初稿の後で修正をお願いする可能性が高いです。)
サイズ
A4
ページ数
片面
希望イメージ
シンプル 複雑
単色 カラフル
暗い 明るい
日常 高級
遊び心 厳粛
未来的 伝統的
女性的 男性的
希望する色
無彩色系
納品ファイル
• PNG形式 (.png)
補足説明
PDFでの納品もお願いしたいです。
サロンロゴのpngデータを添付しました。

スピード感があり、デザインも最初から希望していたものに近かった。

ご提案ありがとうございました!
またぜひよろしくお願いします!

```html
<!DOCTYPE html>
<html lang="ja">
<head>
<meta charset="UTF-8">
<title>髪のフォローアップサロン Tavi グランドオープン</title>
<link href="https://fonts.googleapis.com/css2?family=Cormorant+Garamond:wght@500;600&family=Noto+Serif+JP:wght@500;600&family=Noto+Sans+JP:wght@400;500;700&display=swap" rel="stylesheet">
<style>
:root{
  --paper:#f3f2ef;
  --ink:#2f2f2f;
  --ink-soft:#5a5a5a;
  --line:#9a9a9a;
  --photo-warm:#d9c7b4;
  --photo-cool:#b9bcc0;
  --leaf:#a9b8a4;
  --leaf-pale:#d5ddd1;
  --map:#e2e1dd;
}
*{margin:0;padding:0;box-sizing:border-box}
html,body{width:849px;height:1200px;overflow:hidden;background:var(--paper)}
.flyer{position:relative;width:849px;height:1200px;background:var(--paper);color:var(--ink);font-family:"Noto Sans JP",sans-serif;overflow:hidden}
.leaf{position:absolute;border-radius:50%;opacity:.8}
.leaf--left{left:-60px;top:250px;width:150px;height:380px;background:radial-gradient(ellipse at 60% 50%,var(--leaf) 0%,var(--leaf-pale) 55%,transparent 75%)}
.leaf--right{right:-50px;top:860px;width:160px;height:320px;background:radial-gradient(ellipse at 40% 50%,var(--leaf) 0%,var(--leaf-pale) 55%,transparent 75%)}
.leaf--bottom{left:-40px;bottom:-60px;width:200px;height:160px;background:radial-gradient(ellipse,var(--leaf-pale) 0%,transparent 70%)}
.photo{position:absolute}
.photo--woman{left:28px;top:42px;width:240px;height:230px;border-radius:46% 54% 48% 52%/50% 46% 54% 50%;background:linear-gradient(160deg,#e9e2da,var(--photo-warm))}
.photo--man{left:240px;top:150px;width:290px;height:230px;background:linear-gradient(150deg,#d4d6d8,var(--photo-cool))}
.catch{position:absolute;right:40px;top:40px;writing-mode:vertical-rl;font-family:"Noto Serif JP",serif;font-weight:600;font-size:31px;line-height:1.55;letter-spacing:.12em;height:290px}
.headline{position:absolute;left:62px;top:480px;font-family:"Cormorant Garamond",serif;font-weight:600;font-size:86px;line-height:.98;letter-spacing:.02em}
.date{position:absolute;left:505px;top:420px;width:290px;height:240px}
.date__num{position:absolute;font-family:"Cormorant Garamond",serif;font-weight:500;font-size:210px;line-height:1}
.date__month{left:0;top:0}
.date__day{left:195px;top:35px}
.date__slash{position:absolute;left:100px;top:20px;width:2px;height:210px;background:var(--ink);transform:rotate(28deg);transform-origin:center}
.date__dow{position:absolute;left:118px;top:160px;font-family:"Cormorant Garamond",serif;font-weight:600;font-size:30px;letter-spacing:.05em}
.menu{position:absolute;top:690px;left:62px;width:725px;display:grid;grid-template-columns:1fr 1fr;column-gap:42px;font-size:11.5px;line-height:1.55;color:var(--ink-soft)}
.menu__item{margin-bottom:9px}
.menu__title{display:flex;justify-content:space-between;font-weight:700;font-size:12.5px;color:var(--ink);border-bottom:1px dotted var(--line);padding-bottom:1px;margin-bottom:2px}
.menu__title::before{content:"●";font-size:8px;margin-right:5px;align-self:center}
.menu__title span:first-child{flex:1}
.map{position:absolute;right:52px;top:975px;width:175px;height:125px;background:var(--map);border-radius:4px}
.map svg{position:absolute;left:12px;top:10px}
.reserve{position:absolute;left:62px;top:1115px;font-size:13px;font-weight:500;letter-spacing:.03em}
.footer{position:absolute;left:62px;top:1140px;display:flex;align-items:center;gap:22px}
.brand{display:flex;align-items:center;gap:8px}
.brand__mark{width:12px;height:12px;border-radius:50%;background:var(--ink)}
.brand__text{font-family:"Noto Serif JP",serif;font-weight:600;line-height:1.1}
.brand__sub{display:block;font-size:9px;letter-spacing:.08em}
.brand__name{display:block;font-size:28px;letter-spacing:.06em}
.contact{display:flex;flex-direction:column}
.contact__tel{display:flex;align-items:center;gap:6px;font-size:26px;font-weight:700;letter-spacing:.04em;line-height:1.1}
.contact__addr{font-size:11px;color:var(--ink-soft)}
</style>
</head>
<body>
<main class="flyer">
  <div class="leaf leaf--left" role="img" aria-label="ユーカリの葉の装飾"></div>
  <div class="leaf leaf--right" role="img" aria-label="ユーカリの葉の装飾"></div>
  <div class="leaf leaf--bottom" role="img" aria-label="葉の装飾"></div>

  <div class="photo photo--woman" role="img" aria-label="ショートボブの女性モデルの写真"></div>
  <div class="photo photo--man" role="img" aria-label="ジャケット姿の男性モデルの写真"></div>

  <h2 class="catch">あなたの髪を、<br>毎日サロン帰りの髪に</h2>

  <h1 class="headline">GRAND<br>OPEN!!</h1>

  <div class="date" aria-label="7月1日金曜日">
    <span class="date__num date__month">7</span>
    <span class="date__slash"></span>
    <span class="date__dow">FRI</span>
    <span class="date__num date__day">1</span>
  </div>

  <section class="menu">
    <div class="menu__col">
      <div class="menu__item"><div class="menu__title"><span>ヘアカットコース</span><span>¥4,400</span></div>カウンセリングで髪質を見極め、扱いやすいスタイルに仕上げます。</div>
      <div class="menu__item"><div class="menu__title"><span>ヘアカラーコース</span><span>¥6,600</span></div>ダメージを抑えた薬剤で、透明感のある色味を長く楽しめます。</div>
      <div class="menu__item"><div class="menu__title"><span>スペシャルケアコース</span><span>¥11,000</span></div>髪の内部まで補修し、毎朝のまとまりやすさを実感できます。</div>
      <div class="menu__item"><div class="menu__title"><span>縮毛矯正コース</span><span>¥15,400</span></div>自然なストレートで、湿気の多い日もうねりにくい髪へ。</div>
      <div class="menu__item"><div class="menu__title"><span>ヘッドスパ</span><span>¥3,300</span></div>頭皮の汚れを落とし、健やかな髪が育つ環境を整えます。</div>
    </div>
    <div class="menu__col">
      <div class="menu__item"><div class="menu__title"><span>髪質改善トリートメント</span><span>¥8,800</span></div>あなたの髪に合わせて配合し、指通りの良いツヤ髪に導きます。</div>
      <div class="menu__item"><div class="menu__title"><span>メンズカット</span><span>¥3,850</span></div>骨格に合わせ、セットしやすく清潔感のある印象に整えます。</div>
      <div class="menu__item"><div class="menu__title"><span>ホームケア相談</span><span>無料</span></div>ご自宅でのお手入れ方法を、<br>丁寧にお伝えします。</div>
      <div class="menu__item"><div class="menu__title"><span>フォローアップ</span><span>¥2,200</span></div>施術後の状態を確認し、<br>仕上がりを長持ちさせます。</div>
    </div>
  </section>

  <div class="map" role="img" aria-label="サロン周辺の地図">
    <svg width="18" height="24" viewBox="0 0 18 24" aria-hidden="true"><path d="M9 0C4 0 0 4 0 9c0 6.5 9 15 9 15s9-8.5 9-15c0-5-4-9-9-9z" fill="#2f2f2f"/><circle cx="9" cy="9" r="3.2" fill="#e2e1dd"/></svg>
  </div>

  <p class="reserve">予約受付開始：6月24日(金)　あなたのご来店を楽しみにお待ちしております！</p>

  <footer class="footer">
    <div class="brand">
      <span class="brand__mark"></span>
      <span class="brand__text"><span class="brand__sub">髪のフォローアップサロン</span><span class="brand__name">Tavi</span></span>
    </div>
    <div class="contact">
      <span class="contact__tel">
        <svg width="20" height="20" viewBox="0 0 24 24" aria-hidden="true"><path d="M6.6 10.8a15.1 15.1 0 0 0 6.6 6.6l2.2-2.2a1 1 0 0 1 1-.25 11.4 11.4 0 0 0 3.6.57 1 1 0 0 1 1 1V20a1 1 0 0 1-1 1A17 17 0 0 1 3 4a1 1 0 0 1 1-1h3.5a1 1 0 0 1 1 1c0 1.25.2 2.45.57 3.57a1 1 0 0 1-.25 1z" fill="#2f2f2f"/></svg>
        095-231-4862
      </span>
      <span class="contact__addr">佐賀県佐賀市東原町大字桜沢418-6</span>
    </div>
  </footer>
</main>
</body>
</html>
```